Stationery Design Project

We are looking for a full revision of our existing stationary to include within this project:

- Letterhead
- Business card
- Compliment slip

The items should be a reflection of our new website which can be found at http://www.brackenledger.co.uk/

Our logo files are included within the file brief

There are some further projects which we may approach the winning designer for as we need a revision to the front cover of our reports, a new price list and two brochures for specific target markets.

Industry/Entity Type

Business

```html
<!DOCTYPE html>
<html lang="en">
<head>
<meta charset="utf-8">
<title>Bracken Ledger – Stationery</title>
<link rel="stylesheet" href="https://fonts.googleapis.com/css2?family=Jost:wght@400;500&family=Libre+Baskerville&display=swap">
<style>
  :root {
    --navy: #161c66;
    --blue: #2950a6;
    --paper: #ffffff;
    --ground: #eceef1;
    --ink: #3b3f5c;
    --window: #d7d9de;
  }
  * { box-sizing: border-box; margin: 0; padding: 0; }
  html, body { width: 1200px; height: 795px; overflow: hidden; }
  body { background: var(--ground); font-family: "Jost", sans-serif; color: var(--ink); }
  .canvas { position: relative; width: 1200px; height: 795px; }

  .sheet { position: absolute; background: var(--paper); box-shadow: 0 1px 4px rgba(20,25,60,.12); overflow: hidden; }
  .brand-name { font-family: "Jost", sans-serif; font-weight: 500; color: var(--navy); white-space: nowrap; letter-spacing: .02em; }
  .brand-name.on-dark { color: #fff; }
  .roof-band { position: absolute; left: 0; bottom: 0; width: 100%; }
  .roof-band polygon { fill: var(--navy); }
  .contact { position: absolute; font-size: 5.5px; line-height: 1.55; color: var(--ink); }
  .contact .icon { display: inline-block; width: 4px; height: 4px; background: var(--blue); margin-right: 3px; vertical-align: middle; }

  /* business cards */
  .card { width: 250px; height: 155px; }
  .card-front { left: 90px; top: 40px; background: linear-gradient(135deg, var(--navy), var(--blue)); }
  .card-front .brand-name { position: absolute; left: 0; right: 0; top: 58px; text-align: center; font-size: 22px; }
  .card-front .web { position: absolute; left: 0; right: 0; top: 92px; text-align: center; font-size: 8px; color: #cfd6f0; }
  .card-back { left: 90px; top: 215px; }
  .card-back .brand-name { position: absolute; right: 18px; top: 22px; font-size: 15px; }
  .card-back .person { position: absolute; left: 18px; top: 58px; font-size: 8px; font-weight: 500; color: var(--navy); }
  .card-back .contact { left: 18px; top: 72px; }

  /* letterhead */
  .letterhead { left: 400px; top: 40px; width: 300px; height: 410px; }
  .letterhead .brand-name { position: absolute; left: 22px; top: 22px; font-size: 17px; }
  .letterhead .contact { right: 22px; top: 60px; }

  /* folder */
  .folder { left: 760px; top: 40px; width: 300px; height: 410px; }
  .folder-cover { position: absolute; left: 0; top: 0; width: 100%; height: 200px; }
  .folder-cover polygon { fill: url(#folderGradient); }
  .folder .brand-name { position: absolute; left: 0; right: 0; top: 255px; text-align: center; font-size: 30px; }
  .folder .web { position: absolute; left: 0; right: 0; top: 305px; text-align: center; font-size: 11px; color: var(--navy); letter-spacing: .04em; }

  /* compliment slip */
  .compliment-slip { left: 40px; top: 490px; width: 360px; height: 180px; }
  .compliment-slip .brand-name { position: absolute; left: 150px; top: 20px; font-size: 16px; }
  .compliment-slip .greeting { position: absolute; left: 18px; top: 70px; font-family: "Libre Baskerville", serif; font-size: 8px; color: var(--ink); }
  .compliment-slip .contact { right: 18px; top: 62px; }

  /* envelopes */
  .envelope { width: 360px; height: 180px; }
  .envelope-window { left: 420px; top: 490px; }
  .envelope-window .return-line { position: absolute; left: 20px; top: 20px; font-size: 5.5px; }
  .envelope-window .brand-name { position: absolute; right: 22px; top: 16px; font-size: 15px; }
  .envelope-window .address-window { position: absolute; left: 20px; top: 40px; width: 130px; height: 42px; background: var(--window); border-radius: 2px; }
  .envelope-back { left: 800px; top: 490px; }
  .envelope-back .flap { position: absolute; left: 0; top: 0; width: 100%; height: 70px; }
  .envelope-back .flap polygon { fill: none; stroke: #d9dbe0; stroke-width: 1; }
  .envelope-back .brand-name { position: absolute; left: 0; right: 0; top: 40px; text-align: center; font-size: 18px; }

  .showcase-name { position: absolute; left: 40px; top: 715px; font-size: 24px; }
</style>
</head>
<body>
<div class="canvas">
  <svg width="0" height="0" aria-hidden="true" style="position:absolute">
    <defs>
      <linearGradient id="folderGradient" x1="0" y1="0" x2="1" y2="1">
        <stop offset="0" stop-color="#161c66"/>
        <stop offset="1" stop-color="#2950a6"/>
      </linearGradient>
    </defs>
  </svg>

  <section class="sheet card card-front">
    <div class="brand-name on-dark">Bracken Ledger</div>
    <div class="web">www.brackenledger.co.uk</div>
  </section>

  <section class="sheet card card-back">
    <div class="brand-name">Bracken Ledger</div>
    <div class="person">Alex Morgan</div>
    <div class="contact">
      <div><span class="icon"></span>14 Fernhill Road, Leeds LS6 2QT</div>
      <div><span class="icon"></span>0113 496 0721</div>
      <div><span class="icon"></span>hello@brackenledger.co.uk</div>
    </div>
    <svg class="roof-band" viewBox="0 0 100 20" preserveAspectRatio="none" height="26"><polygon points="0,18 55,18 100,5 100,20 0,20"/></svg>
  </section>

  <section class="sheet letterhead">
    <div class="brand-name">Bracken Ledger</div>
    <div class="contact">
      <div>Bracken Ledger Ltd</div>
      <div>14 Fernhill Road, Leeds LS6 2QT</div>
      <div><span class="icon"></span>0113 496 0721</div>
      <div><span class="icon"></span>hello@brackenledger.co.uk</div>
      <div><span class="icon"></span>www.brackenledger.co.uk</div>
    </div>
    <svg class="roof-band" viewBox="0 0 100 20" preserveAspectRatio="none" height="40"><polygon points="0,18 55,18 100,4 100,20 0,20"/></svg>
  </section>

  <section class="sheet folder">
    <svg class="folder-cover" viewBox="0 0 300 200" preserveAspectRatio="none"><polygon points="0,0 300,0 300,200 240,185 0,140"/></svg>
    <div class="brand-name">Bracken Ledger</div>
    <div class="web">www.brackenledger.co.uk</div>
  </section>

  <section class="sheet compliment-slip">
    <div class="brand-name">Bracken Ledger</div>
    <div class="greeting">With Best Compliments</div>
    <div class="contact">
      <div>14 Fernhill Road, Leeds LS6 2QT</div>
      <div><span class="icon"></span>0113 496 0721</div>
      <div><span class="icon"></span>hello@brackenledger.co.uk</div>
    </div>
    <svg class="roof-band" viewBox="0 0 100 20" preserveAspectRatio="none" height="34"><polygon points="0,18 55,18 100,4 100,20 0,20"/></svg>
  </section>

  <section class="sheet envelope envelope-window">
    <div class="return-line">Bracken Ledger Ltd, 14 Fernhill Road, Leeds LS6 2QT</div>
    <div class="brand-name">Bracken Ledger</div>
    <div class="address-window"></div>
    <svg class="roof-band" viewBox="0 0 100 20" preserveAspectRatio="none" height="34"><polygon points="0,18 55,18 100,4 100,20 0,20"/></svg>
  </section>

  <section class="sheet envelope envelope-back">
    <svg class="flap" viewBox="0 0 360 70" preserveAspectRatio="none"><polygon points="0,0 20,70 340,70 360,0"/></svg>
    <div class="brand-name">Bracken Ledger</div>
  </section>

  <div class="brand-name showcase-name">Bracken Ledger</div>
</div>
</body>
</html>
```